New business card for KT4 Linkway, a marketing company.

We need a new business card design. We would like it to be blue gray and white. We would like some movement but in a more subtle pattern than in the file we uploaded. We are a marketing company that connects brands with their target audiences - we make connections. We work in the New York Metro area with sophisticated clients. The card should feel modern, upscale and professional.

Target Market(s)

Businesses looking to grow their brands in tourism and nightlife. We work with liquor and beer companies and with Tourism bureaus and companies.

Industry/Entity Type

Marketing

Contact Information for Business Card

Would like a horizontal layout, two-sided. Would like the logo on the back with the tagline ' "connecting brands to their target audiences" under the logo. On the front, we would like name, title, contact email, contact phone, website.

Font styles to use
Sans Serif

Colors
3377b5
85cae6
ffffff

Requirements
Must have
• Our logo. See attached. Otherwise, open to your ideas.
Should not have
• No colors we don't want - no reds/pinks/oranges please

```html
<!DOCTYPE html>
<html lang="en">
<head>
<meta charset="utf-8">
<title>KT4 Linkway — Business Card</title>
<link href="https://fonts.googleapis.com/css2?family=Montserrat:wght@400;500&family=Libre+Baskerville&display=swap" rel="stylesheet">
<style>
  :root {
    --brand-blue: #1d5a8e;
    --name-blue: #2f6aa3;
    --ink: #2a2a2a;
    --title-gray: #8a8a8a;
    --card-white: #ffffff;
    --back-gray: #9d9d9d;
    --tagline: #f2f2f2;
  }
  html, body {
    margin: 0;
    padding: 0;
    width: 900px;
    height: 1200px;
    overflow: hidden;
    background: var(--back-gray);
    font-family: "Montserrat", Arial, sans-serif;
  }
  .sheet { position: relative; width: 900px; height: 1200px; }

  /* Front side */
  .card-front {
    position: absolute; left: 0; top: 0; width: 900px; height: 486px;
    background: var(--card-white);
  }
  .front-edge {
    position: absolute; left: 0; top: 486px; width: 900px; height: 8px;
    background: var(--brand-blue);
  }
  .brand-name {
    color: var(--brand-blue); font-weight: 500; letter-spacing: 2px;
    margin: 0; text-align: center; width: 900px; position: absolute; left: 0;
  }
  .front-brand { top: 120px; font-size: 24px; }
  .holder-name {
    position: absolute; top: 276px; width: 900px; text-align: center;
    margin: 0; font-size: 40px; font-weight: 400; color: var(--name-blue);
    letter-spacing: 1px;
  }
  .holder-title {
    position: absolute; top: 324px; width: 900px; text-align: center;
    margin: 0; font-family: "Libre Baskerville", Georgia, serif;
    font-size: 24px; color: var(--title-gray); letter-spacing: 1px;
  }
  .contact-row {
    position: absolute; top: 452px; left: 48px; right: 48px;
    display: flex; justify-content: space-between; align-items: center;
    font-size: 23px; color: var(--ink);
  }
  .contact-item { display: flex; align-items: center; gap: 10px; }
  .contact-item svg { width: 26px; height: 26px; }

  /* Back side */
  .back-band-top {
    position: absolute; left: 0; top: 579px; width: 900px; height: 36px;
    background: var(--brand-blue);
  }
  .back-band-bottom {
    position: absolute; left: 0; top: 1128px; width: 900px; height: 72px;
    background: var(--brand-blue);
  }
  .back-brand { top: 828px; font-size: 68px; font-weight: 500; letter-spacing: 3px; }
  .tagline {
    position: absolute; top: 1060px; width: 900px; text-align: center;
    margin: 0; font-size: 22px; color: var(--tagline); letter-spacing: 0.5px;
  }
  .tagline-dots { font-size: 18px; letter-spacing: 2px; margin-right: 6px; }
</style>
</head>
<body>
<main class="sheet">
  <section class="card-front">
    <p class="brand-name front-brand">KT4 LINKWAY</p>
    <h1 class="holder-name">DANIEL HARTLEY</h1>
    <p class="holder-title">DIRECTOR</p>
    <div class="contact-row">
      <span class="contact-item">
        <svg viewBox="0 0 26 26" aria-hidden="true"><rect width="26" height="26" rx="4" fill="#1d5a8e"/><rect x="5" y="8" width="16" height="11" fill="none" stroke="#fff" stroke-width="1.8"/><path d="M5 8l8 6 8-6" fill="none" stroke="#fff" stroke-width="1.8"/></svg>
        info@kt4linkway.com
      </span>
      <span class="contact-item">
        <svg viewBox="0 0 26 26" aria-hidden="true"><rect width="26" height="26" rx="4" fill="#1d5a8e"/><rect x="8" y="4" width="10" height="18" rx="2" fill="none" stroke="#fff" stroke-width="1.8"/><circle cx="13" cy="18.5" r="1.2" fill="#fff"/></svg>
        917 555 0143
      </span>
      <span class="contact-item">
        <svg viewBox="0 0 26 26" aria-hidden="true"><rect width="26" height="26" rx="4" fill="#1d5a8e"/><circle cx="13" cy="13" r="8" fill="none" stroke="#fff" stroke-width="1.6"/><ellipse cx="13" cy="13" rx="3.5" ry="8" fill="none" stroke="#fff" stroke-width="1.4"/><path d="M5 13h16" stroke="#fff" stroke-width="1.4"/></svg>
        www.kt4linkway.com
      </span>
    </div>
  </section>
  <div class="front-edge"></div>

  <section class="card-back">
    <div class="back-band-top"></div>
    <p class="brand-name back-brand">KT4 LINKWAY</p>
    <p class="tagline"><span class="tagline-dots">•••</span>connecting brands to their target audiences</p>
    <div class="back-band-bottom"></div>
  </section>
</main>
</body>
</html>
```